Elegant, professional powerpoint design for Vellmark Engineering and Mining SARLU

I’ve created a new Sub contracting company for mining industry in the Democratic Republic of Congo. With MotifNest, I’ve created a logo. I would want a professional and beautiful powerpoint design which I will use to sell my services to mining companies in DRC. The powerpoint must have pictures of mining engines such as excavators, drones, trucks, etc

```html
<!DOCTYPE html>
<html lang="en">
<head>
<meta charset="utf-8">
<title>Vellmark Engineering and Mining – Presentation Deck</title>
<link href="https://fonts.googleapis.com/css2?family=Open+Sans:wght@400;600;700&family=Roboto+Slab:wght@400;600&display=swap" rel="stylesheet">
<style>
:root{
  --gold:#d4930f;
  --gold-lt:#f2ac1f;
  --navy:#27339a;
  --violet:#7b80d2;
  --brown:#8f5a0c;
  --slate:#3c3f78;
  --ink:#333;
  --muted:#555;
  --line:#d9d9d9;
  --photo:linear-gradient(180deg,#7fa6cf 0%,#b9cde0 30%,#dba634 52%,#96621b 74%,#4a3d2c 100%);
  --photo-warm:linear-gradient(180deg,#c9baa0 0%,#e3a52a 38%,#b0731b 66%,#3e3528 100%);
  --photo-pit:linear-gradient(180deg,#b9a27c 0%,#98714a 35%,#6f5a43 65%,#463b2d 100%);
}
*{box-sizing:border-box;margin:0;padding:0}
html,body{width:1200px;height:1200px;overflow:hidden;background:#fff;font-family:"Open Sans",sans-serif;color:var(--ink)}
.sheet{position:relative;width:1200px;height:1200px}
.slide{position:absolute;width:234px;height:131px;background:#fff;overflow:hidden;box-shadow:0 3px 12px rgba(0,0,0,.22)}
.c1{left:76px}.c2{left:349px}.c3{left:623px}.c4{left:897px}
.r1{top:34px}.r2{top:178px}.r3{top:321px}.r4{top:466px}.r5{top:609px}.r6{top:754px}.r7{top:898px}.r8{top:1042px}
.foot{position:absolute;left:0;right:0;bottom:0;height:4px;background:linear-gradient(90deg,var(--navy) 77%,var(--gold) 77%);font-size:2.2px;color:#fff;padding-left:10px;line-height:4px}
.foot b{position:absolute;right:6px;font-weight:400}
.t{position:absolute;left:0;right:0;top:13px;text-align:center;font-size:9.5px;color:var(--gold);font-weight:400;line-height:1}
.t.l{text-align:left;left:18px}
.t.dark{color:#222}
.s{position:absolute;left:0;right:0;top:25px;text-align:center;font-size:2.4px;color:#777;letter-spacing:.1px}
.s.l{text-align:left;left:18px}
.logo{position:absolute;right:7px;top:7px;display:flex;flex-direction:column;align-items:center;gap:1px;font-size:3.2px;font-weight:700;color:var(--gold)}
.logo i{display:block;width:7px;height:7px;background:var(--gold);border-radius:50%}
.ph{position:absolute;background:var(--photo)}
.ph.w{background:var(--photo-warm)}
.ph.pit{background:var(--photo-pit)}
.p{font-size:2.8px;line-height:1.38;color:var(--muted)}
.p b{color:#222}
.h{font-size:3.9px;font-weight:700;color:var(--gold)}
.h.n{color:#222}
.abs{position:absolute}
.dot{width:8px;height:8px;border-radius:50%;background:var(--gold);display:block;margin:0 auto 2px;box-shadow:inset 0 0 0 1.6px var(--gold),inset 0 0 0 2.4px #fff}
.dot.n{background:var(--navy);box-shadow:inset 0 0 0 1.6px var(--navy),inset 0 0 0 2.4px #fff}
.dot.v{background:var(--violet);box-shadow:inset 0 0 0 1.6px var(--violet),inset 0 0 0 2.4px #fff}
.col{position:absolute;text-align:center}
.box{position:absolute;padding:3px;color:#fff;font-size:2.8px;line-height:1.38}
.box .h{color:#fff;font-size:3.9px;margin-bottom:2px}
.navy{background:var(--navy)}.gold{background:var(--gold-lt)}.violet{background:var(--violet)}.brown{background:var(--brown)}
svg{position:absolute;overflow:visible}
.tbl{position:absolute;border-collapse:collapse;font-size:2.8px}
.tbl td,.tbl th{border-bottom:.3px solid var(--line);padding:.55px 2px;text-align:center;width:22px}
.tbl th{background:var(--navy);color:#fff;font-weight:400}
.tbl td:first-child{text-align:left;background:#eef;width:18px}
</style>
</head>
<body>
<div class="sheet">

<!-- Row 1 -->
<section class="slide c1 r1">
  <svg width="234" height="131">
    <polygon points="24,45 50,18 90,26 90,68 56,96 24,88" fill="none" stroke="var(--gold)" stroke-width=".6"/>
    <polygon points="66,20 104,36 104,82 70,106 32,92 30,46" fill="var(--gold)"/>
    <defs><linearGradient id="hexph" x1="0" y1="0" x2="0" y2="1"><stop offset="0" stop-color="#b9a27c"/><stop offset=".45" stop-color="#8c6b44"/><stop offset="1" stop-color="#3f352a"/></linearGradient></defs>
    <polygon points="67,25 100,39 100,80 70,101 36,89 34,48" fill="url(#hexph)" role="img" aria-label="Excavator working in open-pit mine"/>
    <polygon points="100,80 126,100 116,120 80,118" fill="none" stroke="var(--navy)" stroke-width=".6"/>
  </svg>
  <div class="abs" style="left:142px;top:29px;font-size:7.5px;font-weight:700;color:var(--gold);display:flex;align-items:center;gap:2px"><i style="width:6px;height:6px;background:var(--gold);display:block"></i>VELLMARK</div>
  <div class="abs" style="left:142px;top:39px;font-size:2.6px;color:var(--gold);font-weight:700">ENGINEERING AND MINING</div>
  <div class="abs" style="left:142px;top:47px;font-family:'Roboto Slab',serif;font-size:5.4px;line-height:1.2;color:var(--gold)">PLACE HERE YOUR<br>TITLE PRESENTATION</div>
  <div class="abs" style="left:142px;top:61px;font-size:3.6px;color:#222">YOUR SUBTITLE SLIDE HERE</div>
  <div class="abs" style="left:142px;top:72px;font-size:3.6px;color:var(--gold)">CLIENT NAME HERE</div>
  <div class="abs" style="left:142px;top:79px;font-size:2.4px;color:var(--gold)">Presented by : Alex Morgan</div>
  <div class="abs" style="left:142px;top:84px;font-size:2.4px;color:var(--gold)">DATE : 20 January 2023</div>
</section>

<section class="slide c2 r1">
  <div class="t">About Vellmark</div><div class="s">LOREM IPSUM, GIVING INFORMATION ON ITS ORIGINS, AS WELL AS A RANDOM TEXT HERE</div>
  <div class="logo"><i></i>VELLMARK</div>
  <div class="col" style="left:22px;top:47px;width:52px"><i class="dot n"></i><div class="h">What we Do</div><p class="p" style="margin-top:6px"><b>Lorem Ipsum</b> is simply dummy text of the printing and typesetting industry. Lorem Ipsum has been the standard text ever.</p></div>
  <div class="col" style="left:91px;top:47px;width:52px"><i class="dot n"></i><div class="h">Our Mission</div><p class="p" style="margin-top:6px"><b>Lorem Ipsum</b> is simply dummy text of the printing and typesetting industry. Lorem Ipsum has been the standard text ever.</p></div>
  <div class="col" style="left:160px;top:47px;width:52px"><i class="dot n"></i><div class="h">Our Vision</div><p class="p" style="margin-top:6px"><b>Lorem Ipsum</b> is simply dummy text of the printing and typesetting industry. Lorem Ipsum has been the standard text ever.</p></div>
  <div class="foot">Confidential – Not for Distribution<b>2</b></div>
</section>

<section class="slide c3 r1">
  <div class="t">Click to edit title slide</div><div class="s">LOREM IPSUM, GIVING INFORMATION ON ITS ORIGINS, AS WELL AS A RANDOM TEXT HERE</div>
  <div class="logo"><i></i>VELLMARK</div>
  <div class="abs h n" style="left:23px;top:42px">Lorem dummy text</div>
  <div class="abs h n" style="left:89px;top:42px">Lorem dummy text</div>
  <div class="abs h n" style="left:155px;top:39px">Lorem dummy text</div>
  <div class="ph" style="left:23px;top:49px;width:57px;height:32px" role="img" aria-label="Haul truck on mine road"></div>
  <div class="ph pit" style="left:89px;top:49px;width:57px;height:32px" role="img" aria-label="Excavator loading rock"></div>
  <div class="ph w" style="left:155px;top:47px;width:57px;height:32px" role="img" aria-label="Articulated dump truck"></div>
  <p class="p abs" style="left:23px;top:89px;width:57px"><b>Lorem Ipsum</b> is simply dummy text of the printing and typesetting industry.</p>
  <p class="p abs" style="left:89px;top:89px;width:57px"><b>Lorem Ipsum</b> is simply dummy text of the printing and typesetting industry.</p>
  <p class="p abs" style="left:155px;top:89px;width:57px"><b>Lorem Ipsum</b> is simply dummy text of the printing and typesetting industry.</p>
  <div class="foot">Confidential – Not for Distribution<b>3</b></div>
</section>

<section class="slide c4 r1">
  <div class="ph w" style="left:112px;top:0;width:122px;height:131px" role="img" aria-label="Worker beside large mining haul truck"></div>
  <svg width="234" height="131"><path d="M112 0 H158 C130 30 150 60 120 90 C110 105 90 120 80 131 H112 Z" fill="#fff"/><path d="M158 0 C130 30 150 60 120 90 C110 105 95 120 84 131" fill="none" stroke="var(--navy)" stroke-width="3"/><path d="M164 0 C138 30 156 62 126 92 C116 107 102 120 92 131" fill="none" stroke="var(--gold)" stroke-width="2"/><rect x="0" y="0" width="112" height="131" fill="#fff"/></svg>
  <div class="t l">Click to edit title slide</div><div class="s l">LOREM IPSUM, GIVING INFORMATION ON ITS ORIGINS, AS WELL AS A RANDOM TEXT HERE</div>
  <p class="p abs" style="left:18px;top:38px;width:92px"><b>Lorem Ipsum</b> is simply dummy text of the printing and typesetting industry. Lorem Ipsum has been the standard dummy text ever.</p>
  <p class="p abs" style="left:18px;top:56px;width:92px">Since the 1500s, an unknown printer took a galley of type and scrambled it to make a type specimen book.</p>
  <p class="p abs" style="left:18px;top:74px;width:92px">But also the leap into electronic typesetting, remaining essentially unchanged.</p>
  <div class="foot" style="background:none;color:#777">Confidential – Not for Distribution</div>
</section>

<!-- Row 2 -->
<section class="slide c1 r2">
  <div class="ph pit" style="left:0;top:0;width:234px;height:55px" role="img" aria-label="Open-pit mine terraces"></div>
  <div class="t l" style="color:#fff;top:11px;font-size:10px">Click to edit title slide</div>
  <div class="s l" style="color:#eee;top:24px">LOREM IPSUM, GIVING INFORMATION ON ITS ORIGINS, AS WELL AS A RANDOM TEXT</div>
  <div class="abs navy" style="left:0;top:49px;width:234px;height:21px"></div>
  <svg width="234" height="131"><g fill="none" stroke="#fff" stroke-width=".7"><circle cx="44" cy="60" r="9"/><circle cx="93" cy="60" r="9"/><circle cx="142" cy="60" r="9"/><circle cx="191" cy="60" r="9"/><path d="M38 60 h3 l1.5-3 2 6 2-5 1 2 h3"/><circle cx="93" cy="60" r="3.5"/><path d="M142 55 a2.5 2.5 0 1 1 -.01 0 M138 64 c1-4 7-4 8 0"/><rect x="187" y="57" width="8" height="6" rx=".5"/></g></svg>
  <div class="col" style="left:26px;top:79px;width:36px"><div class="h">TITLE<br>Text</div><p class="p"><b>Lorem Ipsum</b> is simply dummy text of the printing and typesetting industry.</p></div>
  <div class="col" style="left:75px;top:79px;width:36px"><div class="h">TITLE<br>Text</div><p class="p"><b>Lorem Ipsum</b> is simply dummy text of the printing and typesetting industry.</p></div>
  <div class="col" style="left:124px;top:79px;width:36px"><div class="h">TITLE<br>Text</div><p class="p"><b>Lorem Ipsum</b> is simply dummy text of the printing and typesetting industry.</p></div>
  <div class="col" style="left:173px;top:79px;width:36px"><div class="h">TITLE<br>Text</div><p class="p"><b>Lorem Ipsum</b> is simply dummy text of the printing and typesetting industry.</p></div>
  <div class="foot">Confidential – Not for Distribution<b>5</b></div>
</section>

<section class="slide c2 r2">
  <div class="t">Click to edit title slide</div><div class="s">LOREM IPSUM, GIVING INFORMATION ON ITS ORIGINS, AS WELL AS A RANDOM TEXT HERE</div>
  <div class="logo"><i></i>VELLMARK</div>
  <div class="ph pit" style="left:0;top:38px;width:80px;height:48px" role="img" aria-label="Excavators in quarry"></div>
  <div class="abs navy" style="left:80px;top:38px;width:77px;height:48px;color:#fff;text-align:center;padding-top:9px">
    <svg width="10" height="9" style="position:static;display:block;margin:0 auto 3px"><g fill="none" stroke="#fff" stroke-width=".7"><rect x=".5" y=".5" width="9" height="8"/><path d="M2.5 7 V5 M4.5 7 V3 M6.5 7 V4"/></g></svg>
    <div style="font-size:3.9px;font-weight:700">Click to edit subtitle slide</div><p style="font-size:2.8px;margin-top:3px;padding:0 6px;line-height:1.35"><b>Lorem Ipsum</b> is simply dummy text of the printing and typesetting industry.</p></div>
  <div class="ph" style="left:157px;top:38px;width:77px;height:48px" role="img" aria-label="Yellow loader at mine site"></div>
  <p class="p abs" style="left:24px;top:96px;width:186px;text-align:center"><b>Lorem Ipsum</b> is simply dummy text of the printing and typesetting industry. Lorem Ipsum has been the industry standard dummy text ever since the 1500s, when an unknown printer took a galley of type. It has survived not only five centuries.</p>
  <div class="foot">Confidential – Not for Distribution<b>6</b></div>
</section>

<section class="slide c3 r2">
  <div class="t">What We Do</div><div class="logo"><i></i>VELLMARK</div>
  <div class="abs" style="left:22px;top:32px;width:62px"><i class="dot n" style="margin:0"></i><div class="h" style="margin-top:3px">Lorem dummy text</div><p class="p">Lorem Ipsum is simply dummy text of the printing and typesetting industry. Lorem Ipsum has been.</p></div>
  <div class="abs" style="left:91px;top:32px;width:62px"><i class="dot" style="margin:0"></i><div class="h" style="margin-top:3px">Lorem dummy text</div><p class="p">Lorem Ipsum is simply dummy text of the printing and typesetting industry. Lorem Ipsum has been.</p></div>
  <div class="abs" style="left:160px;top:32px;width:62px"><i class="dot n" style="margin:0"></i><div class="h" style="margin-top:3px">Lorem dummy text</div><p class="p">Lorem Ipsum is simply dummy text of the printing and typesetting industry. Lorem Ipsum has been.</p></div>
  <div class="abs" style="left:22px;top:75px;width:62px"><i class="dot" style="margin:0"></i><div class="h" style="margin-top:3px">Lorem dummy text</div><p class="p">Lorem Ipsum is simply dummy text of the printing and typesetting industry. Lorem Ipsum has been.</p></div>
  <div class="abs" style="left:91px;top:75px;width:62px"><i class="dot n" style="margin:0"></i><div class="h" style="margin-top:3px">Lorem dummy text</div><p class="p">Lorem Ipsum is simply dummy text of the printing and typesetting industry. Lorem Ipsum has been.</p></div>
  <div class="abs" style="left:160px;top:75px;width:62px"><i class="dot" style="margin:0"></i><div class="h" style="margin-top:3px">Lorem dummy text</div><p class="p">Lorem Ipsum is simply dummy text of the printing and typesetting industry. Lorem Ipsum has been.</p></div>
  <div class="foot">Confidential – Not for Distribution<b>7</b></div>
</section>

<section class="slide c4 r2">
  <div class="ph w" style="left:130px;top:0;width:104px;height:131px" role="img" aria-label="Front view of mining haul truck"></div>
  <div class="t l">What we Do</div><div class="s l" style="width:100px">LOREM IPSUM, GIVING INFORMATION ON ITS ORIGINS, AS WELL AS A RANDOM TEXT HERE</div>
  <div class="abs" style="left:26px;top:41px;width:98px"><div class="h">Lorem dummy text</div><p class="p"><b>Lorem Ipsum</b> is simply dummy text of the printing and typesetting industry.</p></div>
  <div class="abs" style="left:26px;top:63px;width:98px"><div class="h">Lorem dummy text</div><p class="p"><b>Lorem Ipsum</b> is simply dummy text of the printing and typesetting industry.</p></div>
  <div class="abs" style="left:26px;top:86px;width:98px"><div class="h">Lorem dummy text</div><p class="p"><b>Lorem Ipsum</b> is simply dummy text of the printing and typesetting industry.</p></div>
  <svg width="234" height="131"><g fill="none" stroke="var(--gold)" stroke-width=".6"><circle cx="21" cy="45" r="2.6"/><path d="M21 43.5 v1.5 h1"/><circle cx="21" cy="67" r="2.6"/><path d="M18.4 67 h5.2 M21 64.4 v5.2"/><circle cx="21" cy="90" r="2.6"/><path d="M22.8 91.8 l1.6 1.6"/></g><g stroke="var(--line)" stroke-width=".3"><line x1="18" y1="58" x2="124" y2="58"/><line x1="18" y1="81" x2="124" y2="81"/></g></svg>
  <div class="foot" style="background:none;color:#777">Confidential – Not for Distribution</div>
</section>

<!-- Row 3 -->
<section class="slide c1 r3">
  <div class="t">Click to edit title slide</div><div class="s">LOREM IPSUM, GIVING INFORMATION ON ITS ORIGINS, AS WELL AS A RANDOM TEXT HERE</div>
  <div class="logo"><i></i>VELLMARK</div>
  <div class="box navy" style="left:22px;top:39px;width:62px;height:35px"><div class="h">Title</div><b>Lorem Ipsum</b> is simply dummy text of the printing and typesetting industry.</div>
  <div class="box gold" style="left:84px;top:39px;width:62px;height:35px"><div class="h">Title</div><b>Lorem Ipsum</b> is simply dummy text of the printing and typesetting industry.</div>
  <div class="box violet" style="left:146px;top:39px;width:62px;height:35px"><div class="h">Title</div><b>Lorem Ipsum</b> is simply dummy text of the printing and typesetting industry.</div>
  <div class="box gold" style="left:22px;top:75px;width:62px;height:35px"><div class="h">Title</div><b>Lorem Ipsum</b> is simply dummy text of the printing and typesetting industry.</div>
  <div class="box violet" style="left:84px;top:75px;width:62px;height:35px"><div class="h">Title</div><b>Lorem Ipsum</b> is simply dummy text of the printing and typesetting industry.</div>
  <div class="box brown" style="left:146px;top:75px;width:62px;height:35px"><div class="h">Title</div><b>Lorem Ipsum</b> is simply dummy text of the printing and typesetting industry.</div>
  <div class="foot">Confidential – Not for Distribution<b>9</b></div>
</section>

<section class="slide c2 r3">
  <div class="t">Click to edit title slide</div><div class="s">LOREM IPSUM, GIVING INFORMATION ON ITS ORIGINS, AS WELL AS A RANDOM TEXT HERE</div>
  <div class="logo"><i></i>VELLMARK</div>
  <div class="box navy" style="left:56px;top:38px;width:52px;height:37px;border-radius:0 6px 6px 0;padding-left:12px"><div class="h">Title</div><b>Lorem Ipsum</b> is simply dummy text of the printing.</div>
  <div class="ph" style="left:23px;top:38px;width:42px;height:37px;border-radius:6px" role="img" aria-label="Dump truck on site"></div>
  <div class="box" style="left:150px;top:38px;width:56px;height:37px;border-radius:0 6px 6px 0;padding-left:12px;background:var(--gold)"><div class="h">Title</div><b>Lorem Ipsum</b> is simply dummy text of the printing.</div>
  <div class="ph pit" style="left:118px;top:38px;width:42px;height:37px;border-radius:6px" role="img" aria-label="Excavator in pit"></div>
  <div class="box gold" style="left:56px;top:79px;width:52px;height:37px;border-radius:0 6px 6px 0;padding-left:12px"><div class="h">Title</div><b>Lorem Ipsum</b> is simply dummy text of the printing.</div>
  <div class="ph w" style="left:23px;top:79px;width:42px;height:37px;border-radius:6px" role="img" aria-label="Mining truck at quarry"></div>
  <div class="box violet" style="left:150px;top:79px;width:56px;height:37px;border-radius:0 6px 6px 0;padding-left:12px"><div class="h">Title</div><b>Lorem Ipsum</b> is simply dummy text of the printing.</div>
  <div class="ph" style="left:118px;top:79px;width:42px;height:37px;border-radius:6px" role="img" aria-label="Loader machines at mine"></div>
  <div class="foot">Confidential – Not for Distribution<b>10</b></div>
</section>

<section class="slide c3 r3">
  <div class="t">What people say about Us</div><div class="s">LOREM IPSUM, GIVING INFORMATION ON ITS ORIGINS, AS WELL AS A RANDOM TEXT HERE</div>
  <div class="logo"><i></i>VELLMARK</div>
  <svg width="234" height="131"><g><ellipse cx="55" cy="62" rx="27" ry="18" fill="var(--navy)"/><path d="M42 76 l-4 10 10-7z" fill="var(--navy)"/><ellipse cx="119" cy="62" rx="27" ry="18" fill="var(--gold-lt)"/><path d="M106 76 l-4 10 10-7z" fill="var(--gold-lt)"/><ellipse cx="184" cy="62" rx="27" ry="18" fill="var(--brown)"/><path d="M171 76 l-4 10 10-7z" fill="var(--brown)"/></g><g fill="#6d6d6d"><circle cx="33" cy="95" r="5"/><circle cx="98" cy="95" r="5"/><circle cx="162" cy="95" r="5"/></g></svg>
  <p class="abs" style="left:33px;top:51px;width:44px;font-size:2.8px;color:#fff;text-align:center;line-height:1.35">Lorem Ipsum is simply dummy text of the printing and typesetting industry standard.</p>
  <p class="abs" style="left:97px;top:51px;width:44px;font-size:2.8px;color:#fff;text-align:center;line-height:1.35">Lorem Ipsum is simply dummy text of the printing and typesetting industry standard.</p>
  <p class="abs" style="left:162px;top:51px;width:44px;font-size:2.8px;color:#fff;text-align:center;line-height:1.35">Lorem Ipsum is simply dummy text of the printing and typesetting industry standard.</p>
  <div class="abs" style="left:41px;top:92px;font-size:3.2px;font-weight:700;color:var(--navy)">Name Surname<br><span style="color:var(--gold);font-size:2.6px">Position</span></div>
  <div class="abs" style="left:106px;top:92px;font-size:3.2px;font-weight:700;color:var(--navy)">Name Surname<br><span style="color:var(--gold);font-size:2.6px">Position</span></div>
  <div class="abs" style="left:170px;top:92px;font-size:3.2px;font-weight:700;color:var(--navy)">Name Surname<br><span style="color:var(--gold);font-size:2.6px">Position</span></div>
  <div class="foot">Confidential – Not for Distribution<b>11</b></div>
</section>

<section class="slide c4 r3">
  <div class="t">What people say about Us</div><div class="s">LOREM IPSUM, GIVING INFORMATION ON ITS ORIGINS, AS WELL AS A RANDOM TEXT HERE</div>
  <div class="logo"><i></i>VELLMARK</div>
  <p class="p abs" style="left:24px;top:39px;width:57px;font-style:italic"><b>Lorem Ipsum</b> is simply dummy text of the printing and typesetting industry. Lorem Ipsum has been the industry standard dummy text ever since the 1500s.</p>
  <p class="p abs" style="left:89px;top:39px;width:57px;font-style:italic"><b>Lorem Ipsum</b> is simply dummy text of the printing and typesetting industry. Lorem Ipsum has been the industry standard dummy text ever since the 1500s.</p>
  <p class="p abs" style="left:154px;top:39px;width:57px;font-style:italic"><b>Lorem Ipsum</b> is simply dummy text of the printing and typesetting industry. Lorem Ipsum has been the industry standard dummy text ever since the 1500s.</p>
  <div class="ph w" style="left:24px;top:86px;width:15px;height:15px" role="img" aria-label="Client photo placeholder"></div>
  <div class="ph w" style="left:89px;top:88px;width:15px;height:15px" role="img" aria-label="Client photo placeholder"></div>
  <div class="ph w" style="left:154px;top:86px;width:15px;height:15px" role="img" aria-label="Client photo placeholder"></div>
  <div class="abs" style="left:42px;top:85px;font-size:3.2px;font-weight:700;color:var(--gold)">Name Surname<br><span style="font-size:2.6px;font-weight:400">Position</span></div>
  <div class="abs" style="left:107px;top:87px;font-size:3.2px;font-weight:700;color:var(--gold)">Name Surname<br><span style="font-size:2.6px;font-weight:400">Position</span></div>
  <div class="abs" style="left:172px;top:85px;font-size:3.2px;font-weight:700;color:var(--gold)">Name Surname<br><span style="font-size:2.6px;font-weight:400">Position</span></div>
  <div class="foot">Confidential – Not for Distribution<b>12</b></div>
</section>

<!-- Row 4 -->
<section class="slide c1 r4">
  <div class="ph w" style="left:0;top:0;width:116px;height:131px" role="img" aria-label="Worker in front of large haul truck"></div>
  <svg width="234" height="131"><path d="M136 32 a4.5 4 0 1 1 0.1 0 M133 36 l-2.5 3.5 4.5-2z" fill="var(--navy)"/></svg>
  <p class="abs" style="left:130px;top:48px;width:84px;font-size:3.8px;font-style:italic;color:var(--navy);line-height:1.42"><b>Lorem Ipsum</b> is simply dummy text of the printing and typesetting industry. Lorem Ipsum has been the industry standard dummy text ever since the 1500s.</p>
  <div class="abs" style="left:130px;top:77px;font-size:3.9px;font-weight:700">Alex Morgan</div>
  <div class="abs" style="left:130px;top:83px;font-size:2.4px;color:var(--gold)">company@domain.com</div>
  <div class="abs" style="left:176px;top:124px;font-size:2.2px;color:#555">www.vellmarkmining.com | 13</div>
</section>

<section class="slide c2 r4">
  <div class="t">Why Us ?</div><div class="s">LOREM IPSUM, GIVING INFORMATION ON ITS ORIGINS, AS WELL AS A RANDOM TEXT HERE</div>
  <div class="logo"><i></i>VELLMARK</div>
  <svg width="234" height="131"><polygon points="117,52 134,62 134,82 117,92 100,82 100,62" fill="none" stroke="var(--gold)" stroke-width="3"/><polygon points="117,60 127,66 127,78 117,84 107,78 107,66" fill="var(--brown)"/>
    <rect x="72" y="44" width="12" height="12" rx="2" fill="var(--gold-lt)"/><rect x="72" y="69" width="12" height="12" rx="2" fill="var(--navy)"/><rect x="72" y="94" width="12" height="12" rx="2" fill="var(--violet)"/>
    <rect x="150" y="44" width="12" height="12" rx="2" fill="var(--navy)"/><rect x="150" y="69" width="12" height="12" rx="2" fill="var(--gold-lt)"/><rect x="150" y="94" width="12" height="12" rx="2" fill="var(--brown)"/>
    <g fill="#fff"><path d="M79 46 l-3 5 h2.5 l-1.5 4 4-5.5 h-2.5z"/><path d="M75 72 v6 M75 72 h5 v3.5 h-5"/><rect x="75" y="72" width="5" height="3.5"/><path d="M75 103 l4-6 3 3z"/><rect x="153" y="47" width="6" height="6" fill="none" stroke="#fff" stroke-width=".6"/><path d="M156 71 v8 M152 75 h8 l-3-2 M154 78 l2 1 2-1"/><rect x="152" y="97" width="6" height="4"/><rect x="158" y="98.5" width="2.5" height="2.5"/><circle cx="154" cy="102" r="1"/><circle cx="159" cy="102" r="1"/></g></svg>
  <div class="abs" style="left:16px;top:41px;width:52px;text-align:right"><div class="h n" style="font-weight:400">Title</div><p class="p"><b>Lorem Ipsum</b> is simply dummy text of the printing and typesetting.</p></div>
  <div class="abs" style="left:16px;top:66px;width:52px;text-align:right"><div class="h n" style="font-weight:400">Title</div><p class="p"><b>Lorem Ipsum</b> is simply dummy text of the printing and typesetting.</p></div>
  <div class="abs" style="left:16px;top:91px;width:52px;text-align:right"><div class="h n" style="font-weight:400">Title</div><p class="p"><b>Lorem Ipsum</b> is simply dummy text of the printing and typesetting.</p></div>
  <div class="abs" style="left:166px;top:41px;width:52px"><div class="h n" style="font-weight:400">Title</div><p class="p"><b>Lorem Ipsum</b> is simply dummy text of the printing and typesetting.</p></div>
  <div class="abs" style="left:166px;top:66px;width:52px"><div class="h n" style="font-weight:400">Title</div><p class="p"><b>Lorem Ipsum</b> is simply dummy text of the printing and typesetting.</p></div>
  <div class="abs" style="left:166px;top:91px;width:52px"><div class="h n" style="font-weight:400">Title</div><p class="p"><b>Lorem Ipsum</b> is simply dummy text of the printing and typesetting.</p></div>
  <div class="foot">Confidential – Not for Distribution<b>14</b></div>
</section>

<section class="slide c3 r4">
  <div class="t" style="font-size:10.5px;top:12px">Our services</div><div class="logo"><i></i>VELLMARK</div>
  <div class="col" style="left:23px;top:33px;width:64px"><i class="dot n"></i><div class="h">Lorem dummy text</div><p class="p" style="margin-top:3px">Lorem Ipsum is simply dummy text of the printing and typesetting industry. Lorem Ipsum has been.</p></div>
  <div class="col" style="left:85px;top:33px;width:64px"><i class="dot"></i><div class="h">Lorem dummy text</div><p class="p" style="margin-top:3px">Lorem Ipsum is simply dummy text of the printing and typesetting industry. Lorem Ipsum has been.</p></div>
  <div class="col" style="left:147px;top:33px;width:64px"><i class="dot v"></i><div class="h">Lorem dummy text</div><p class="p" style="margin-top:3px">Lorem Ipsum is simply dummy text of the printing and typesetting industry. Lorem Ipsum has been.</p></div>
  <div class="col" style="left:23px;top:73px;width:64px"><i class="dot"></i><div class="h">Lorem dummy text</div><p class="p" style="margin-top:3px">Lorem Ipsum is simply dummy text of the printing and typesetting industry. Lorem Ipsum has been.</p></div>
  <div class="col" style="left:85px;top:73px;width:64px"><i class="dot n"></i><div class="h">Lorem dummy text</div><p class="p" style="margin-top:3px">Lorem Ipsum is simply dummy text of the printing and typesetting industry. Lorem Ipsum has been.</p></div>
  <div class="col" style="left:147px;top:73px;width:64px"><i class="dot"></i><div class="h">Lorem dummy text</div><p class="p" style="margin-top:3px">Lorem Ipsum is simply dummy text of the printing and typesetting industry. Lorem Ipsum has been.</p></div>
  <div class="foot">Confidential – Not for Distribution<b>16</b></div>
</section>

<section class="slide c4 r4">
  <div class="t">Our TOP 3 services</div><div class="s">LOREM IPSUM, GIVING INFORMATION ON ITS ORIGINS, AS WELL AS A RANDOM TEXT HERE</div>
  <div class="logo"><i></i>VELLMARK</div>
  <div class="ph" style="left:24px;top:39px;width:57px;height:33px" role="img" aria-label="Haul truck on mine road"></div>
  <div class="ph w" style="left:88px;top:39px;width:57px;height:33px" role="img" aria-label="Loader in open pit"></div>
  <div class="ph pit" style="left:152px;top:39px;width:57px;height:33px" role="img" aria-label="Excavator loading truck"></div>
  <svg width="234" height="131"><g fill="#555"><path d="M49 72 h8 l-4 4z"/><path d="M113 72 h8 l-4 4z"/><path d="M177 72 h8 l-4 4z"/></g></svg>
  <div class="abs" style="left:26px;top:78px;width:55px"><div class="h" style="color:var(--navy);text-align:center">Lorem dummy text</div><p class="p">• Lorem ipsum is simply dummy text of the printing.<br>• Lorem ipsum is simply dummy text of the printing.<br>• Lorem ipsum is simply dummy text.</p></div>
  <div class="abs" style="left:90px;top:78px;width:55px"><div class="h" style="color:var(--navy);text-align:center">Lorem dummy text</div><p class="p">• Lorem ipsum is simply dummy text of the printing.<br>• Lorem ipsum is simply dummy text of the printing.<br>• Lorem ipsum is simply dummy text.</p></div>
  <div class="abs" style="left:154px;top:78px;width:55px"><div class="h" style="color:var(--navy);text-align:center">Lorem dummy text</div><p class="p">• Lorem ipsum is simply dummy text of the printing.<br>• Lorem ipsum is simply dummy text of the printing.<br>• Lorem ipsum is simply dummy text.</p></div>
  <div class="foot">Confidential – Not for Distribution<b>17</b></div>
</section>

<!-- Row 5 -->
<section class="slide c1 r5">
  <div class="t l dark">Meet Our Team</div><div class="s l">LOREM IPSUM, GIVING INFORMATION ON ITS ORIGINS, AS WELL AS A RANDOM TEXT HERE</div>
  <div class="logo"><i></i>VELLMARK</div>
  <div class="ph w" style="left:18px;top:39px;width:36px;height:32px" role="img" aria-label="Team member photo placeholder"></div>
  <div class="box navy" style="left:54px;top:39px;width:63px;height:32px"><div class="h" style="margin-bottom:0">Name Surname</div><span style="font-size:2.2px">Marketing Manager</span><br><b>Lorem Ipsum</b> is simply dummy text of the printing industry.</div>
  <div class="ph" style="left:117px;top:39px;width:36px;height:32px" role="img" aria-label="Team member photo placeholder"></div>
  <div class="box gold" style="left:153px;top:39px;width:63px;height:32px"><div class="h" style="margin-bottom:0">Name Surname</div><span style="font-size:2.2px">Marketing Manager</span><br><b>Lorem Ipsum</b> is simply dummy text of the printing industry.</div>
  <div class="box brown" style="left:18px;top:78px;width:63px;height:32px"><div class="h" style="margin-bottom:0">Name Surname</div><span style="font-size:2.2px">Marketing Manager</span><br><b>Lorem Ipsum</b> is simply dummy text of the printing industry.</div>
  <div class="ph w" style="left:81px;top:78px;width:36px;height:32px" role="img" aria-label="Team member photo placeholder"></div>
  <div class="box violet" style="left:117px;top:78px;width:63px;height:32px"><div class="h" style="margin-bottom:0">Name Surname</div><span style="font-size:2.2px">Marketing Manager</span><br><b>Lorem Ipsum</b> is simply dummy text of the printing industry.</div>
  <div class="ph w" style="left:180px;top:78px;width:36px;height:32px" role="img" aria-label="Team member photo placeholder"></div>
  <div class="foot">Confidential – Not for Distribution<b>18</b></div>
</section>

<section class="slide c2 r5">
  <div class="t dark">S.W.O.T Analysis</div><div class="s">LOREM IPSUM, GIVING INFORMATION ON ITS ORIGINS</div>
  <div class="logo"><i></i>VELLMARK</div>
  <svg width="234" height="131"><rect x="62" y="42" width="22" height="22" rx="3" fill="var(--navy)"/><rect x="40" y="56" width="22" height="22" rx="3" fill="var(--gold-lt)"/><rect x="84" y="58" width="22" height="22" rx="3" fill="var(--gold-lt)"/><rect x="60" y="72" width="22" height="22" rx="3" fill="var(--violet)"/>
    <g fill="#fff"><circle cx="62" cy="60" r="3"/><circle cx="84" cy="62" r="3"/><circle cx="71" cy="72" r="3" fill="var(--navy)"/></g>
    <g font-family="Open Sans" font-size="9" fill="#fff" text-anchor="middle"><text x="73" y="57">W</text><text x="51" y="70">S</text><text x="95" y="73">O</text><text x="71" y="88">T</text></g>
    <g stroke="#555" stroke-width=".3"><line x1="84" y1="50" x2="124" y2="50"/><line x1="62" y1="66" x2="124" y2="66"/><line x1="106" y1="70" x2="124" y2="82"/><line x1="82" y1="86" x2="124" y2="98"/></g>
    <g font-family="Open Sans" font-size="9" text-anchor="middle"><text x="130" y="53" fill="var(--navy)">S</text><text x="130" y="69" fill="var(--gold)">W</text><text x="130" y="85" fill="var(--gold-lt)">O</text><text x="130" y="101" fill="var(--navy)">T</text></g></svg>
  <p class="p abs" style="left:138px;top:47px;width:58px">Lorem ipsum dolor sit amet, consectetuer adipiscing elit. Aenean.</p>
  <p class="p abs" style="left:138px;top:63px;width:58px">Lorem ipsum dolor sit amet, consectetuer adipiscing elit. Aenean.</p>
  <p class="p abs" style="left:138px;top:79px;width:58px">Lorem ipsum dolor sit amet, consectetuer adipiscing elit. Aenean.</p>
  <p class="p abs" style="left:138px;top:95px;width:58px">Lorem ipsum dolor sit amet, consectetuer adipiscing elit. Aenean.</p>
  <div class="foot">Confidential – Not for Distribution<b>19</b></div>
</section>

<section class="slide c3 r5">
  <div class="t">Services Option list</div><div class="s">LOREM IPSUM, GIVING INFORMATION ON ITS ORIGINS, AS WELL AS A RANDOM TEXT HERE</div>
  <div class="logo"><i></i>VELLMARK</div>
  <div class="abs" style="left:28px;top:39px;width:42px;height:76px;border:.4px solid var(--line);padding:3px"><div style="font-size:8.5px;line-height:1.1">01</div><p class="p" style="color:#333"><b>Lorem Ipsum</b> is simply dummy text of the printing and typesetting industry. Lorem Ipsum has been the industry standard dummy text ever since the 1500s.</p></div>
  <div class="abs" style="left:73px;top:39px;width:42px;height:76px;border:.4px solid var(--line);padding:3px"><div style="font-size:8.5px;line-height:1.1">02</div><p class="p" style="color:#333"><b>Lorem Ipsum</b> is simply dummy text of the printing and typesetting industry. Lorem Ipsum has been the industry standard dummy text ever since the 1500s.</p></div>
  <div class="abs" style="left:118px;top:39px;width:42px;height:76px;border:.4px solid var(--line);padding:3px"><div style="font-size:8.5px;line-height:1.1;color:var(--violet)">03</div><p class="p" style="color:#333"><b>Lorem Ipsum</b> is simply dummy text of the printing and typesetting industry. Lorem Ipsum has been the industry standard dummy text ever since the 1500s.</p></div>
  <div class="abs" style="left:163px;top:39px;width:42px;height:76px;border:.4px solid var(--line);padding:3px"><div style="font-size:8.5px;line-height:1.1">04</div><p class="p" style="color:#333"><b>Lorem Ipsum</b> is simply dummy text of the printing and typesetting industry. Lorem Ipsum has been the industry standard dummy text ever since the 1500s.</p></div>
  <div class="box navy" style="left:28px;top:108px;width:42px;height:7px;padding:0;line-height:7px;text-align:center;font-size:3.6px">Option name</div>
  <div class="box brown" style="left:73px;top:108px;width:42px;height:7px;padding:0;line-height:7px;text-align:center;font-size:3.6px">Option name</div>
  <div class="box violet" style="left:118px;top:108px;width:42px;height:7px;padding:0;line-height:7px;text-align:center;font-size:3.6px">Option name</div>
  <div class="box brown" style="left:163px;top:108px;width:42px;height:7px;padding:0;line-height:7px;text-align:center;font-size:3.6px">Option name</div>
  <div class="foot">Confidential – Not for Distribution<b>20</b></div>
</section>

<section class="slide c4 r5">
  <div class="t">One column text Slide</div><div class="s">LOREM IPSUM, GIVING INFORMATION ON ITS ORIGINS, AS WELL AS A RANDOM TEXT HERE</div>
  <div class="logo"><i></i>VELLMARK</div>
  <p class="p abs" style="left:18px;top:34px;width:198px;font-size:2.5px;line-height:1.36">Lorem Ipsum is simply dummy text of the printing and typesetting industry. Lorem Ipsum has been the industry standard dummy text ever since the 1500s, when an unknown printer took a galley of type and scrambled it to make a type specimen book. It has survived not only five centuries, but also the leap into electronic typesetting, remaining essentially unchanged. It was popularised in the 1960s with the release of sheets containing Lorem Ipsum passages.<br><br>Contrary to popular belief, Lorem Ipsum is not simply random text. It has roots in a piece of classical Latin literature from 45 BC, making it over 2000 years old. A Latin professor looked up one of the more obscure Latin words and going through the cites of the word in classical literature, discovered the undoubtable source. This book is a treatise on the theory of ethics, very popular during the Renaissance.<br><br>Contrary to popular belief, Lorem Ipsum is not simply random text. It has roots in a piece of classical Latin literature, making it over 2000 years old. The standard chunk used since the 1500s is reproduced below for those interested.</p>
  <div class="foot">Confidential – Not for Distribution<b>21</b></div>
</section>

<!-- Row 6 -->
<section class="slide c1 r6">
  <div class="t">Two column text Slide</div><div class="s">LOREM IPSUM, GIVING INFORMATION ON ITS ORIGINS, AS WELL AS A RANDOM TEXT HERE</div>
  <div class="logo"><i></i>VELLMARK</div>
  <p class="p abs" style="left:18px;top:34px;width:96px;font-size:2.4px">Lorem Ipsum is simply dummy text of the printing and typesetting industry. Lorem Ipsum has been the industry standard dummy text ever since the 1500s, when an unknown printer took a galley of type and scrambled it to make a type specimen book.<br><br>Contrary to popular belief, Lorem Ipsum is not simply random text. It has roots in a piece of classical Latin literature from 45 BC, making it over 2000 years old. It survived five centuries and the leap into electronic typesetting, remaining essentially unchanged through desktop publishing software.</p>
  <p class="p abs" style="left:120px;top:34px;width:96px;font-size:2.4px">Lorem Ipsum is simply dummy text of the printing and typesetting industry. Lorem Ipsum has been the industry standard dummy text ever since the 1500s, when an unknown printer took a galley of type and scrambled it to make a type specimen book.<br><br>Contrary to popular belief, Lorem Ipsum is not simply random text. It has roots in a piece of classical Latin literature from 45 BC, making it over 2000 years old. It survived five centuries and the leap into electronic typesetting, remaining essentially unchanged through desktop publishing software.</p>
  <div class="foot">Confidential – Not for Distribution<b>22</b></div>
</section>

<section class="slide c2 r6">
  <div class="t">Three column text Slide</div><div class="s">LOREM IPSUM, GIVING INFORMATION ON ITS ORIGINS, AS WELL AS A RANDOM TEXT HERE</div>
  <div class="logo"><i></i>VELLMARK</div>
  <p class="p abs" style="left:18px;top:34px;width:62px;font-size:2.4px">Lorem Ipsum is simply dummy text of the printing and typesetting industry. It has been the standard dummy text ever since the 1500s, when an unknown printer took a galley of type.<br><br>Contrary to popular belief, Lorem Ipsum is not simply random text. It has roots in classical Latin literature from 45 BC, making it over 2000 years old, and it was popular during the Renaissance.</p>
  <p class="p abs" style="left:86px;top:34px;width:62px;font-size:2.4px">Lorem Ipsum is simply dummy text of the printing and typesetting industry. It has been the standard dummy text ever since the 1500s, when an unknown printer took a galley of type.<br><br>Contrary to popular belief, Lorem Ipsum is not simply random text. It has roots in classical Latin literature from 45 BC, making it over 2000 years old, and it was popular during the Renaissance.</p>
  <p class="p abs" style="left:154px;top:34px;width:62px;font-size:2.4px">Lorem Ipsum is simply dummy text of the printing and typesetting industry. It has been the standard dummy text ever since the 1500s, when an unknown printer took a galley of type.<br><br>Contrary to popular belief, Lorem Ipsum is not simply random text. It has roots in classical Latin literature from 45 BC, making it over 2000 years old, and it was popular during the Renaissance.</p>
  <div class="foot">Confidential – Not for Distribution<b>23</b></div>
</section>

<section class="slide c3 r6">
  <div class="t dark">Business Plan</div><div class="s">LOREM IPSUM, GIVING INFORMATION ON ITS ORIGINS, AS WELL AS A RANDOM TEXT HERE</div>
  <div class="logo"><i></i>VELLMARK</div>
  <svg width="234" height="131"><g font-family="Open Sans" font-size="4.4" font-weight="700" fill="#fff" text-anchor="middle"><circle cx="44" cy="63" r="21" fill="var(--navy)"/><circle cx="81" cy="63" r="21" fill="var(--brown)"/><circle cx="118" cy="63" r="21" fill="var(--violet)"/><circle cx="155" cy="63" r="21" fill="var(--slate)"/><circle cx="192" cy="63" r="21" fill="var(--gold-lt)"/><text x="44" y="71">Title</text><text x="81" y="71">Title</text><text x="118" y="71">Title</text><text x="155" y="71">Title</text><text x="192" y="71">Title</text></g><g fill="none" stroke="#fff" stroke-width=".6"><rect x="42" y="53" width="4" height="5"/><circle cx="81" cy="56" r="2.6"/><ellipse cx="118" cy="56" rx="3" ry="1.8"/><path d="M152 57 a3 3 0 0 1 6 0z M155 57 v2.5"/><rect x="189.5" y="54" width="5" height="4"/></g></svg>
  <p class="p abs" style="left:29px;top:89px;width:30px;text-align:center;color:#333">Lorem ipsum dolor sit amet, consectetur adipiscing elit. Nam id pulvinar neque.</p>
  <p class="p abs" style="left:66px;top:89px;width:30px;text-align:center;color:#333">Lorem ipsum dolor sit amet, consectetur adipiscing elit. Nam id pulvinar neque.</p>
  <p class="p abs" style="left:103px;top:89px;width:30px;text-align:center;color:#333">Lorem ipsum dolor sit amet, consectetur adipiscing elit. Nam id pulvinar neque.</p>
  <p class="p abs" style="left:140px;top:89px;width:30px;text-align:center;color:#333">Lorem ipsum dolor sit amet, consectetur adipiscing elit. Nam id pulvinar neque.</p>
  <p class="p abs" style="left:177px;top:89px;width:30px;text-align:center;color:#333">Lorem ipsum dolor sit amet, consectetur adipiscing elit. Nam id pulvinar neque.</p>
  <div class="foot">Confidential – Not for Distribution<b>37</b></div>
</section>

<section class="slide c4 r6">
  <div class="t l">Data chart</div><div class="s l">LOREM IPSUM, GIVING INFORMATION ON ITS ORIGINS, AS WELL AS A RANDOM TEXT HERE</div>
  <div class="logo"><i></i>VELLMARK</div>
  <svg width="234" height="131"><g fill="none" stroke-width="3"><circle cx="40" cy="58" r="14" stroke="#eee"/><path d="M40 44 a14 14 0 0 1 0 28" stroke="var(--brown)"/><circle cx="88" cy="58" r="14" stroke="#eee"/><path d="M88 44 a14 14 0 0 1 13.3 18.3" stroke="var(--navy)"/><circle cx="136" cy="58" r="14" stroke="#eee"/><path d="M136 44 a14 14 0 0 1 8.2 2.7" stroke="var(--gold-lt)"/><circle cx="184" cy="58" r="14" stroke="#eee"/><path d="M184 44 a14 14 0 0 1 8.2 25.3" stroke="var(--violet)"/></g><g font-family="Open Sans" font-size="6.4" font-weight="700" text-anchor="middle" fill="#222"><text x="40" y="60.5">50%</text><text x="88" y="60.5">30%</text><text x="136" y="60.5">10%</text><text x="184" y="60.5">40%</text></g></svg>
  <div class="abs" style="left:22px;top:82px;width:38px"><div class="h" style="color:var(--violet);font-weight:400">Data title here</div><p class="p">A peep at some distant orb has power to raise and purify our thoughts.</p></div>
  <div class="abs" style="left:70px;top:82px;width:38px"><div class="h" style="color:var(--navy);font-weight:400">Data title here</div><p class="p">A peep at some distant orb has power to raise and purify our thoughts.</p></div>
  <div class="abs" style="left:118px;top:82px;width:38px"><div class="h" style="color:var(--violet);font-weight:400">Data title here</div><p class="p">A peep at some distant orb has power to raise and purify our thoughts.</p></div>
  <div class="abs" style="left:166px;top:82px;width:38px"><div class="h" style="color:var(--navy);font-weight:400">Data title here</div><p class="p">A peep at some distant orb has power to raise and purify our thoughts.</p></div>
  <div class="foot">Confidential – Not for Distribution<b>27</b></div>
</section>

<!-- Row 7 -->
<section class="slide c1 r7">
  <div class="t">Master Table</div><div class="s">LOREM IPSUM, GIVING INFORMATION ON ITS ORIGINS, AS WELL AS A RANDOM TEXT HERE</div>
  <div class="logo"><i></i>VELLMARK</div>
  <table class="tbl" style="left:18px;top:34px">
    <tr><th style="background:#fff"></th><th>Columna 1</th><th>Columna 2</th><th>Columna 3</th><th>Columna 4</th><th>Columna 5</th><th>Columna 6</th></tr>
    <tr><td>Fila 01</td><td>48</td><td>66</td><td>75</td><td>45</td><td>66</td><td>34</td></tr>
    <tr><td>Fila 02</td><td>35</td><td>75</td><td>89</td><td>58</td><td>48</td><td>66</td></tr>
    <tr><td>Fila 03</td><td>66</td><td>34</td><td>55</td><td>35</td><td>35</td><td>55</td></tr>
    <tr><td>Fila 04</td><td>55</td><td>70</td><td>84</td><td>52</td><td>55</td><td>35</td></tr>
    <tr><td>Fila 05</td><td>48</td><td>66</td><td>75</td><td>45</td><td>66</td><td>34</td></tr>
    <tr><td>Fila 06</td><td>35</td><td>75</td><td>89</td><td>58</td><td>48</td><td>66</td></tr>
    <tr><td>Fila 07</td><td>66</td><td>34</td><td>55</td><td>35</td><td>35</td><td>55</td></tr>
    <tr><td>Fila 08</td><td>55</td><td>70</td><td>84</td><td>52</td><td>55</td><td>35</td></tr>
    <tr><td>Fila 09</td><td>48</td><td>66</td><td>75</td><td>45</td><td>66</td><td>34</td></tr>
    <tr><td>Total Columnas</td><td>456</td><td>556</td><td>681</td><td>425</td><td>474</td><td>454</td></tr>
  </table>
  <div class="foot">Confidential – Not for Distribution<b>35</b></div>
</section>

<section class="slide c2 r7">
  <div class="t">Gantt Chart Slide</div><div class="s">LOREM IPSUM, GIVING INFORMATION ON ITS ORIGINS, AS WELL AS A RANDOM TEXT HERE</div>
  <div class="logo"><i></i>VELLMARK</div>
  <svg width="234" height="131"><rect x="18" y="36" width="200" height="4" fill="var(--slate)"/><rect x="18" y="40" width="18" height="80" fill="var(--violet)"/>
    <g stroke="#ddd" stroke-width=".25"><line x1="18" y1="46" x2="218" y2="46"/><line x1="18" y1="52" x2="218" y2="52"/><line x1="18" y1="58" x2="218" y2="58"/><line x1="18" y1="64" x2="218" y2="64"/><line x1="18" y1="70" x2="218" y2="70"/><line x1="18" y1="76" x2="218" y2="76"/><line x1="18" y1="82" x2="218" y2="82"/><line x1="18" y1="88" x2="218" y2="88"/><line x1="18" y1="94" x2="218" y2="94"/><line x1="18" y1="100" x2="218" y2="100"/><line x1="18" y1="106" x2="218" y2="106"/><line x1="18" y1="112" x2="218" y2="112"/>
    <line x1="50" y1="40" x2="50" y2="120"/><line x1="80" y1="40" x2="80" y2="120"/><line x1="110" y1="40" x2="110" y2="120"/><line x1="140" y1="40" x2="140" y2="120"/><line x1="170" y1="40" x2="170" y2="120"/><line x1="200" y1="40" x2="200" y2="120"/></g>
    <rect x="38" y="41" width="50" height="3.2" fill="var(--navy)"/><rect x="80" y="47" width="50" height="3.2" fill="var(--violet)"/><rect x="50" y="59" width="110" height="3.2" fill="var(--violet)"/><rect x="115" y="71" width="100" height="3.2" fill="var(--navy)"/><rect x="58" y="95" width="22" height="3.2" fill="var(--gold-lt)"/><rect x="106" y="107" width="88" height="3.2" fill="var(--brown)"/>
    <g font-family="Open Sans" font-size="2.6" fill="#fff"><text x="20" y="39">2023</text><text x="20" y="44">Enero</text><text x="20" y="50">Febrero</text><text x="20" y="56">Marzo</text><text x="20" y="62">Abril</text><text x="20" y="68">Mayo</text><text x="20" y="74">Junio</text><text x="20" y="80">Julio</text><text x="20" y="86">Agosto</text><text x="20" y="92">Sept.</text><text x="20" y="98">Octubre</text><text x="20" y="104">Nov.</text><text x="20" y="110">Dic.</text><text x="60" y="43.6">Texto</text><text x="100" y="49.6">Texto</text><text x="100" y="61.6">Texto</text><text x="160" y="73.6">Texto</text><text x="65" y="97.6">Texto</text><text x="145" y="109.6">Texto</text></g></svg>
  <div class="foot">Confidential – Not for Distribution<b>34</b></div>
</section>

<section class="slide c3 r7">
  <div class="t l">Clustered Bar Style</div><div class="s l">LOREM IPSUM, GIVING INFORMATION ON ITS ORIGINS, AS WELL AS A RANDOM TEXT HERE</div>
  <div class="logo"><i></i>VELLMARK</div>
  <div class="abs" style="left:18px;top:44px;width:68px"><div class="h n" style="font-weight:700">Your Subtitle here</div><p class="p" style="color:#333;margin-top:2px"><b>Lorem Ipsum is simply dummy text of the printing and typesetting industry.</b><br><br><b>Lorem Ipsum has been the industry standard.</b><br><br>A peep at some distant orb has power to raise and purify our thoughts like a strain of sacred music.</p></div>
  <svg width="234" height="131"><g stroke="#ddd" stroke-width=".25"><line x1="102" y1="48" x2="102" y2="112"/></g>
    <rect x="102" y="52" width="72" height="2.5" fill="var(--navy)"/><rect x="102" y="55" width="42" height="2.5" fill="var(--gold-lt)"/><rect x="102" y="58" width="60" height="2.5" fill="#aaa"/>
    <rect x="102" y="67" width="55" height="2.5" fill="var(--navy)"/><rect x="102" y="70" width="28" height="2.5" fill="var(--gold-lt)"/><rect x="102" y="73" width="60" height="2.5" fill="#aaa"/>
    <rect x="102" y="82" width="48" height="2.5" fill="var(--navy)"/><rect x="102" y="85" width="60" height="2.5" fill="var(--gold-lt)"/><rect x="102" y="88" width="35" height="2.5" fill="#aaa"/>
    <rect x="102" y="97" width="40" height="2.5" fill="var(--navy)"/><rect x="102" y="100" width="80" height="2.5" fill="var(--gold-lt)"/><rect x="102" y="103" width="30" height="2.5" fill="#aaa"/>
    <g font-family="Open Sans" font-size="2.2" fill="#777"><text x="87" y="57">Category 4</text><text x="87" y="72">Category 3</text><text x="87" y="87">Category 2</text><text x="87" y="102">Category 1</text><text x="130" y="43">■ Series 1  ■ Series 2  ■ Series 3</text><text x="102" y="116">0</text><text x="132" y="116">2</text><text x="162" y="116">4</text><text x="192" y="116">6</text></g></svg>
  <div class="foot">Confidential – Not for Distribution<b>32</b></div>
</section>

<section class="slide c4 r7">
  <div class="t l">Stacked Bar Style</div><div class="s l">LOREM IPSUM, GIVING INFORMATION ON ITS ORIGINS, AS WELL AS A RANDOM TEXT HERE</div>
  <div class="logo"><i></i>VELLMARK</div>
  <div class="abs" style="left:18px;top:44px;width:68px"><div class="h n" style="font-weight:700">Your Subtitle here</div><p class="p" style="color:#333;margin-top:2px"><b>Lorem Ipsum is simply dummy text of the printing and typesetting industry.</b><br><br><b>Lorem Ipsum has been the industry standard.</b><br><br>A peep at some distant orb has power to raise and purify our thoughts like a strain of sacred music.</p></div>
  <svg width="234" height="131"><line x1="98" y1="48" x2="98" y2="114" stroke="#ddd" stroke-width=".25"/>
    <rect x="98" y="55" width="30" height="5" fill="var(--navy)"/><rect x="128" y="55" width="18" height="5" fill="var(--gold-lt)"/><rect x="146" y="55" width="34" height="5" fill="var(--violet)"/>
    <rect x="98" y="72" width="22" height="5" fill="var(--navy)"/><rect x="120" y="72" width="12" height="5" fill="var(--gold-lt)"/><rect x="132" y="72" width="24" height="5" fill="var(--violet)"/>
    <rect x="98" y="89" width="26" height="5" fill="var(--navy)"/><rect x="124" y="89" width="28" height="5" fill="var(--gold-lt)"/><rect x="152" y="89" width="22" height="5" fill="var(--violet)"/>
    <rect x="98" y="106" width="32" height="5" fill="var(--navy)"/><rect x="130" y="106" width="14" height="5" fill="var(--gold-lt)"/><rect x="144" y="106" width="12" height="5" fill="var(--violet)"/>
    <g font-family="Open Sans" font-size="2.2" fill="#fff"><text x="110" y="58.5">4.3</text><text x="134" y="58.5">2.4</text><text x="161" y="58.5">5</text><text x="106" y="75.5">2.5</text><text x="123" y="75.5">4.4</text><text x="142" y="75.5">2</text></g>
    <g font-family="Open Sans" font-size="2.2" fill="#777"><text x="84" y="58.5">Category 4</text><text x="84" y="75.5">Category 3</text><text x="84" y="92.5">Category 2</text><text x="84" y="109.5">Category 1</text><text x="122" y="43">■ Series 1  ■ Series 2  ■ Series 3</text></g></svg>
  <div class="foot">Confidential – Not for Distribution<b>31</b></div>
</section>

<!-- Row 8 -->
<section class="slide c1 r8">
  <div class="t l">Data Overview</div><div class="s l">LOREM IPSUM, GIVING INFORMATION ON ITS ORIGINS, AS WELL AS A RANDOM TEXT HERE</div>
  <div class="logo"><i></i>VELLMARK</div>
  <div class="abs" style="left:18px;top:46px;width:68px"><div class="h n" style="font-weight:700">Your Subtitle here</div><p class="p" style="color:#333;margin-top:2px"><b>Lorem Ipsum is simply dummy text of the printing and typesetting industry.</b><br><br><b>Lorem Ipsum has been the industry standard.</b><br><br>A peep at some distant orb has power to raise and purify our thoughts like a strain of sacred music.</p></div>
  <svg width="234" height="131"><g stroke="#e3e3e3" stroke-width=".25"><line x1="100" y1="62" x2="210" y2="62"/><line x1="100" y1="78" x2="210" y2="78"/><line x1="100" y1="94" x2="210" y2="94"/></g><line x1="100" y1="110" x2="210" y2="110" stroke="#ccc" stroke-width=".3"/>
    <g><rect x="107" y="75" width="4" height="35" fill="var(--navy)"/><rect x="112" y="93" width="4" height="17" fill="var(--gold-lt)"/><rect x="117" y="92" width="4" height="18" fill="var(--brown)"/>
    <rect x="133" y="82" width="4" height="28" fill="var(--navy)"/><rect x="138" y="72" width="4" height="38" fill="var(--gold-lt)"/><rect x="143" y="94" width="4" height="16" fill="var(--brown)"/>
    <rect x="159" y="79" width="4" height="31" fill="var(--navy)"/><rect x="164" y="90" width="4" height="20" fill="var(--gold-lt)"/><rect x="169" y="86" width="4" height="24" fill="var(--brown)"/>
    <rect x="185" y="72" width="4" height="38" fill="var(--navy)"/><rect x="190" y="88" width="4" height="22" fill="var(--gold-lt)"/><rect x="195" y="62" width="4" height="48" fill="var(--brown)"/></g>
    <g font-family="Open Sans" font-size="2.2" fill="#777"><text x="107" y="114">Category 1</text><text x="133" y="114">Category 2</text><text x="159" y="114">Category 3</text><text x="185" y="114">Category 4</text><text x="130" y="42">■ Series 1  ■ Series 2  ■ Series 3</text></g></svg>
  <div class="foot">Confidential – Not for Distribution<b>30</b></div>
</section>

<section class="slide c2 r8">
  <div class="t l">Data Overview</div><div class="s l">LOREM IPSUM, GIVING INFORMATION ON ITS ORIGINS, AS WELL AS A RANDOM TEXT HERE</div>
  <div class="logo"><i></i>VELLMARK</div>
  <div class="abs" style="left:18px;top:46px;width:68px"><div class="h n" style="font-weight:700">Your Subtitle here</div><p class="p" style="color:#333;margin-top:2px"><b>Lorem Ipsum is simply dummy text of the printing and typesetting industry.</b><br><br><b>Lorem Ipsum has been the industry standard.</b><br><br>A peep at some distant orb has power to raise and purify our thoughts like a strain of sacred music.</p></div>
  <svg width="234" height="131"><path d="M165 78 L165 56 A22 22 0 1 1 145 90 Z" fill="var(--navy)"/><path d="M163 78 L143 88 A22 22 0 0 1 141 66 Z" fill="var(--violet)"/><path d="M162 76 L141 64 A22 22 0 0 1 152 54 Z" fill="#555"/><path d="M163 76 L154 53 A22 22 0 0 1 163 52 Z" fill="#bbb"/>
    <g font-family="Open Sans" font-size="2.6" fill="#555"><text x="190" y="80">2016 58%</text><text x="127" y="90">2017 23%</text><text x="132" y="54">2018 10%</text><text x="155" y="47">2019 9%</text><text x="143" y="119">■ 2016 ■ 2017 ■ 2018 ■ 2019</text></g></svg>
  <div class="foot">Confidential – Not for Distribution<b>29</b></div>
</section>

<section class="slide c3 r8">
  <div class="t l">Data chart # 2</div><div class="s l">LOREM IPSUM, GIVING INFORMATION ON ITS ORIGINS, AS WELL AS A RANDOM TEXT HERE</div>
  <div class="logo"><i></i>VELLMARK</div>
  <svg width="234" height="131"><g fill="none" stroke-width="2.4"><circle cx="41" cy="58" r="11" stroke="#eee"/><path d="M41 47 a11 11 0 0 1 6.5 2.1" stroke="var(--brown)"/><circle cx="115" cy="58" r="11" stroke="#eee"/><path d="M115 47 a11 11 0 1 1 -6.5 2.1" stroke="var(--violet)"/><circle cx="189" cy="56" r="11" stroke="#eee"/><path d="M189 45 a11 11 0 1 1 -11 11" stroke="var(--gold-lt)"/><circle cx="78" cy="86" r="11" stroke="#eee"/><path d="M78 75 a11 11 0 0 1 8.9 17.5" stroke="var(--gold)"/><circle cx="152" cy="86" r="11" stroke="#eee"/><path d="M152 75 a11 11 0 0 1 10.9 12.4" stroke="var(--navy)"/></g>
    <g font-family="Open Sans" font-size="5.6" font-weight="700" text-anchor="middle"><text x="41" y="60" fill="#222">10%</text><text x="115" y="60" fill="var(--violet)">90%</text><text x="189" y="58" fill="var(--gold-lt)">75%</text><text x="78" y="88" fill="#222">35%</text><text x="152" y="88" fill="var(--navy)">23%</text></g></svg>
  <div class="abs" style="left:64px;top:47px;width:32px"><div class="h" style="color:var(--violet);font-weight:400;font-size:3.2px">Data title here</div><p class="p" style="font-size:2.4px">A peep at some distant orb has power to raise and purify.</p></div>
  <div class="abs" style="left:138px;top:47px;width:32px"><div class="h" style="color:var(--violet);font-weight:400;font-size:3.2px">Data title here</div><p class="p" style="font-size:2.4px">A peep at some distant orb has power to raise and purify.</p></div>
  <div class="abs" style="left:27px;top:77px;width:32px"><div class="h" style="color:var(--violet);font-weight:400;font-size:3.2px">Data title here</div><p class="p" style="font-size:2.4px">A peep at some distant orb has power to raise and purify.</p></div>
  <div class="abs" style="left:101px;top:77px;width:32px"><div class="h" style="color:var(--violet);font-weight:400;font-size:3.2px">Data title here</div><p class="p" style="font-size:2.4px">A peep at some distant orb has power to raise and purify.</p></div>
  <div class="abs" style="left:175px;top:77px;width:32px"><div class="h" style="color:var(--violet);font-weight:400;font-size:3.2px">Data title here</div><p class="p" style="font-size:2.4px">A peep at some distant orb has power to raise and purify.</p></div>
  <div class="foot">Confidential – Not for Distribution<b>28</b></div>
</section>

<section class="slide c4 r8">
  <div class="ph" style="left:0;top:0;width:104px;height:131px" role="img" aria-label="Large yellow excavator at mine site"></div>
  <div class="abs" style="left:123px;top:13px;font-size:10.5px;color:var(--gold)">Contact Us</div>
  <div class="logo"><i></i>VELLMARK</div>
  <svg width="234" height="131"><g fill="none" stroke="var(--navy)" stroke-width=".5"><rect x="123" y="40" width="8" height="8" rx="1"/><rect x="123" y="55" width="8" height="8" rx="1"/><rect x="123" y="70" width="8" height="8" rx="1"/><rect x="123" y="85" width="8" height="8" rx="1"/><rect x="123" y="100" width="8" height="8" rx="1"/></g>
    <g fill="var(--navy)"><path d="M127 41.5 a2 2 0 0 1 2 2 c0 1.5-2 3.5-2 3.5 s-2-2-2-3.5 a2 2 0 0 1 2-2z"/><path d="M125 57 l1.5 0 1 1.5-.8 .8 1.5 1.5.8-.8 1.5 1 0 1.5c-3 0-5.5-2.5-5.5-5.5z"/><rect x="125.5" y="71.5" width="3" height="5" rx=".5"/><rect x="124.5" y="87" width="5" height="3.5"/><rect x="124.5" y="102" width="5" height="3.5"/></g><path d="M124.5 87 l2.5 2 2.5-2" stroke="#fff" stroke-width=".4" fill="none"/></svg>
  <div class="abs" style="left:136px;top:41px;font-size:2.8px;color:var(--gold);width:72px;line-height:1.3">Lorem ipsum dolor sit amet, consectetuer adipiscing elit.</div>
  <div class="abs" style="left:136px;top:58px;font-size:2.8px;color:var(--gold)">+1 234 567 890</div>
  <div class="abs" style="left:136px;top:73px;font-size:2.8px">+1 234 567 890</div>
  <div class="abs" style="left:136px;top:88px;font-size:2.8px">name@domainname.com</div>
  <div class="abs" style="left:136px;top:103px;font-size:2.8px">www.domainname.com</div>
</section>

</div>
</body>
</html>
```